Flash Banner Ad for web advertising

We are a float centre in Auckland, New Zealand. Please see our website at www.tidepoolrest.co.nz for more info on us and what we provide

We need an HTML5 flash ad for various websites promoting our product that generates traffic onto our website.

Dimensions (W x H): 300x250 pixels
Max File Size: 80 kB
Format: HTML5

This banner needs to be brief (3-4 slides) and visual, with booking being the last slide. Should say that the product provides relaxation and other benefits as can be seen on home page of our site. Needs to be a summary as people do not look at banners for long.

Please use images attached or images from our site, please message if you need more resources:
https://www.filecrate.example/sh/qk7ztw31bnxa9pe/BBRwLmcd8hs2XoTkeyGjd4Lpe?dl=0

Target Market(s)

Stressed individuals who need a break from every day life.

Industry/Entity Type

Health And Wellness

Colors
3176b5
0592cd
34a7d8
add136
9bcb3c
33b8a4
ffffff

Requirements
Must have
• Slides that finish into a website book now link

```html
<!DOCTYPE html>
<html lang="en">
<head>
<meta charset="utf-8">
<title>Tidepool Rest – Web Banner Variants</title>
<link rel="stylesheet" href="https://fonts.googleapis.com/css2?family=Roboto:wght@300&family=Source+Sans+3:wght@700&display=swap">
<style>
  :root {
    --page-bg: #ffffff;
    --page-glow: #ececec;
    --night-deep: #0f1030;
    --night-mid: #1a1f55;
    --night-water: #1f3a9a;
    --ink-white: #ffffff;
    --button-navy: #1d1b4b;
    --ocean-dark: #08558a;
    --ocean-light: #1079c0;
    --lime-dark: #86a70e;
    --lime-light: #b3d337;
    --accent-blue: #1a78c2;
    --accent-lime: #9bcb3c;
  }
  * { margin: 0; padding: 0; box-sizing: border-box; }
  html, body { width: 1200px; height: 1000px; overflow: hidden; }
  body {
    position: relative;
    background: radial-gradient(ellipse 70% 60% at 50% 50%, var(--page-bg) 55%, var(--page-glow) 100%);
    font-family: "Roboto", Arial, sans-serif;
  }
  .banner {
    position: absolute;
    top: 277px;
    width: 504px;
    height: 420px;
    overflow: hidden;
  }
  .banner--ocean { left: 91px; --accent: var(--accent-blue); }
  .banner--lime { left: 618px; --accent: var(--accent-lime); }
  .banner__art { position: absolute; inset: 0; width: 504px; height: 420px; display: block; }
  .brand {
    position: absolute;
    left: 24px;
    top: 22px;
    display: flex;
    align-items: center;
    gap: 14px;
    color: var(--ink-white);
    font-family: "Roboto", Arial, sans-serif;
    font-weight: 300;
    font-size: 42px;
    letter-spacing: 0.5px;
    white-space: nowrap;
  }
  .brand__ring {
    width: 74px;
    height: 74px;
    border: 2px solid var(--ink-white);
    border-radius: 50%;
    flex: none;
  }
  .benefits {
    position: absolute;
    left: 25px;
    top: 122px;
    list-style: none;
  }
  .benefits__item {
    display: flex;
    align-items: center;
    gap: 10px;
    height: 38px;
    color: var(--ink-white);
    font-weight: 300;
    font-size: 22px;
  }
  .benefits__mark {
    width: 23px;
    height: 23px;
    border: 2px solid var(--accent);
    border-radius: 50%;
    flex: none;
  }
  .cta {
    position: absolute;
    left: 340px;
    top: 348px;
    width: 142px;
    height: 48px;
    border-radius: 8px;
    background: var(--button-navy);
    color: var(--ink-white);
    font-family: "Source Sans 3", Arial, sans-serif;
    font-weight: 700;
    font-size: 16px;
    display: flex;
    align-items: center;
    justify-content: center;
    text-decoration: none;
    letter-spacing: 0.2px;
  }
</style>
</head>
<body>

<section class="banner banner--ocean" aria-label="Tidepool Rest banner, blue variant">
  <svg class="banner__art" viewBox="0 0 504 420" xmlns="http://www.w3.org/2000/svg">
    <defs>
      <linearGradient id="nightOcean" x1="0" y1="0" x2="1" y2="1">
        <stop offset="0" stop-color="#0f1030"/>
        <stop offset="0.55" stop-color="#1a1f55"/>
        <stop offset="1" stop-color="#1f3a9a"/>
      </linearGradient>
      <linearGradient id="oceanBand" x1="1" y1="0" x2="0.6" y2="1">
        <stop offset="0" stop-color="#08558a"/>
        <stop offset="1" stop-color="#1079c0"/>
      </linearGradient>
    </defs>
    <rect width="504" height="420" fill="url(#nightOcean)" role="img" aria-label="Photo of a woman floating calmly on her back in a dark blue-lit float tank"/>
    <path d="M0,306 C150,345 380,322 504,176 L504,420 L0,420 Z" fill="#ffffff"/>
    <path d="M0,333 C165,350 392,332 504,186 L504,420 L0,420 Z" fill="url(#oceanBand)"/>
  </svg>
  <div class="brand"><span class="brand__ring"></span>Tidepool Rest</div>
  <ul class="benefits">
    <li class="benefits__item"><span class="benefits__mark"></span>Deep Relaxation</li>
    <li class="benefits__item"><span class="benefits__mark"></span>Self-Discovery</li>
    <li class="benefits__item"><span class="benefits__mark"></span>Stress Relief</li>
    <li class="benefits__item"><span class="benefits__mark"></span>Relieves Pain</li>
  </ul>
  <a class="cta" href="https://www.tidepoolrest.co.nz">BOOK NOW</a>
</section>

<section class="banner banner--lime" aria-label="Tidepool Rest banner, green variant">
  <svg class="banner__art" viewBox="0 0 504 420" xmlns="http://www.w3.org/2000/svg">
    <defs>
      <linearGradient id="nightLime" x1="0" y1="0" x2="1" y2="1">
        <stop offset="0" stop-color="#0f1030"/>
        <stop offset="0.55" stop-color="#1a1f55"/>
        <stop offset="1" stop-color="#1f3a9a"/>
      </linearGradient>
      <linearGradient id="limeBand" x1="1" y1="0" x2="0.6" y2="1">
        <stop offset="0" stop-color="#86a70e"/>
        <stop offset="1" stop-color="#b3d337"/>
      </linearGradient>
    </defs>
    <rect width="504" height="420" fill="url(#nightLime)" role="img" aria-label="Photo of a woman floating calmly on her back in a dark blue-lit float tank"/>
    <path d="M0,306 C150,345 380,322 504,176 L504,420 L0,420 Z" fill="#ffffff"/>
    <path d="M0,333 C165,350 392,332 504,186 L504,420 L0,420 Z" fill="url(#limeBand)"/>
  </svg>
  <div class="brand"><span class="brand__ring"></span>Tidepool Rest</div>
  <ul class="benefits">
    <li class="benefits__item"><span class="benefits__mark"></span>Deep Relaxation</li>
    <li class="benefits__item"><span class="benefits__mark"></span>Self-Discovery</li>
    <li class="benefits__item"><span class="benefits__mark"></span>Stress Relief</li>
    <li class="benefits__item"><span class="benefits__mark"></span>Relieves Pain</li>
  </ul>
  <a class="cta" href="https://www.tidepoolrest.co.nz">BOOK NOW</a>
</section>

</body>
</html>
```